Start-up consultancy in Healthcare Space requiring clean and crisp website design

I am the founder of a start-up consultancy to improve access to medicines and healthcare around the globe. My primary product are consulting services to both the public sector and the private sector to work on: improved healthcare delivery, the right price for medicines and addressing challenges in emerging markets. As the sector is fairly conservative, I need a clean and very professional website as is should signal competence in the sector. Therefore, I like shades of white and green but there should be a link to healthcare. Please see the logo that is featured on my business cards.

Target Market(s)

Ministry of Health, Pharmaceutical companies, Emerging Markets (Latin America, Middle East, Eastern Europe, Asia)

Industry/Entity Type

Healthcare

Coding

Coded - Design and coding required

Number of Pages Required

5+ page

Font styles to use
Serif

Colors

Designer to choose colors to be used in the design.

Requirements
Must have
• About Section
• Services Section
• Blog Section
• The website design should also portray the solution for access to healthcare and highlight my ability to help clients with that.
• The website will be hosted on a CMS and should therefore be easy to adjust. I would prefer wordpress but open to any suggestions as I have my own webspace.
• I quite like these websites:
• https://www.velmorhub.com/why-tandri
• https://home.quillstonecare.com/
Nice to have
• I like to see some creative thinking with the theme of healthcare.
Should not have
• The design should not feature too many hospitals or pills etc. as this is really not my focus.

```html
<!DOCTYPE html>
<html lang="en">
<head>
<meta charset="utf-8">
<title>Halvren Consulting</title>
<link href="https://fonts.googleapis.com/css2?family=Noto+Serif:wght@400;700&family=Roboto:wght@400;500&family=Poppins:wght@400;500&display=swap" rel="stylesheet">
<style>
:root{
  --teal:#17a58c;
  --teal-soft:#d9f2ec;
  --orange:#f37321;
  --peach:#fde5d6;
  --ink:#1f1f1f;
  --muted:#666;
  --grey-bg:#f4f4f4;
  --footer:#1e1d2a;
  --footer-text:#b9b9c3;
  --serif:'Noto Serif', Georgia, serif;
  --sans:'Roboto', Arial, sans-serif;
  --ui:'Poppins', Arial, sans-serif;
}
*{margin:0;padding:0;box-sizing:border-box}
html,body{width:1200px;height:2848px;overflow:hidden;background:#fff}
body{position:relative;font-family:var(--sans);color:var(--ink)}
h1,h2,h3,h4{font-weight:400}
.abs{position:absolute}
a{color:inherit;text-decoration:none}

/* header */
.site-header{position:absolute;left:0;top:0;width:1200px;height:72px;background:#fff}
.nav-link{position:absolute;top:27px;font-size:13px;font-family:var(--ui);white-space:nowrap}
.nav-link.active{color:var(--teal)}
.brand{position:absolute;left:515px;top:22px;display:flex;align-items:center;gap:9px;font-family:var(--ui);font-weight:500;font-size:20px;color:var(--ink)}
.brand-dot{width:14px;height:14px;border-radius:50%;background:var(--teal)}
.quote-link{position:absolute;left:910px;top:27px;font-size:13px;font-family:var(--ui);border-bottom:1px solid var(--ink);padding-bottom:2px}
.contact-btn{position:absolute;left:1010px;top:15px;width:101px;height:40px;background:var(--orange);color:#fff;font-size:13px;font-family:var(--ui);display:flex;align-items:center;justify-content:center}

/* hero */
.hero{position:absolute;left:0;top:72px;width:1200px;height:498px;background:linear-gradient(90deg,#d8d4cc 0%,#ece9e3 45%,#eeece8 100%)}
.hero-photo{position:absolute;left:57px;top:50px;width:480px;height:448px;background:radial-gradient(ellipse at 50% 60%,#c9b48d 0%,#b7a889 45%,rgba(200,190,170,0) 75%)}
.hero-title{position:absolute;left:640px;top:160px;font-family:var(--serif);font-weight:700;font-size:34px;line-height:50px;color:#222;white-space:nowrap}
.hero-btn{position:absolute;left:640px;top:283px;width:101px;height:38px;background:var(--teal);color:#fff;font-size:13px;display:flex;align-items:center;justify-content:center}
.hero-dots span{position:absolute;left:1147px;width:6px;height:6px;border-radius:50%;background:#bbb}

/* shared */
.rule{position:absolute;height:2px;width:44px;background:var(--teal)}
.section-title{position:absolute;width:1200px;left:0;text-align:center;font-family:var(--serif);font-size:23px}

/* intro */
.intro-title{position:absolute;left:89px;top:686px;font-family:var(--serif);font-size:23px;line-height:31px}
.intro-text{position:absolute;left:89px;width:440px;font-size:13px;line-height:23px;color:var(--muted)}
.peach-btn{position:absolute;left:89px;top:953px;width:112px;height:38px;background:var(--peach);color:var(--orange);font-size:13px;display:flex;align-items:center;justify-content:center}
.media{position:absolute}

/* services */
.services{position:absolute;left:0;top:1090px;width:1200px;height:418px;background:var(--orange);color:#fff}
.service-icon{position:absolute;width:90px;height:90px;border-radius:46% 54% 42% 58%/52% 44% 56% 48%;background:#fff;top:175px;display:flex;align-items:center;justify-content:center}
.service-label{position:absolute;top:285px;width:300px;text-align:center;font-size:16px}
.dotline{position:absolute;top:218px;height:4px;background:radial-gradient(circle,#f9b58b 2px,transparent 2.5px) 0 0/17px 4px}

/* blogs */
.blog-card{position:absolute;top:1662px;width:323px;height:391px;background:#fff;border:1px solid #e6e6e6}
.blog-card.lifted{box-shadow:0 12px 30px rgba(0,0,0,.12);border-color:#eee}
.blog-img{width:100%;height:207px}
.blog-date{position:absolute;left:26px;top:233px;font-size:15px;line-height:23px;border-right:1px solid #ddd;padding-right:10px}
.blog-date b{display:block;color:var(--teal);font-weight:500}
.blog-date b.warm{color:var(--orange)}
.blog-heading{position:absolute;left:82px;top:236px;font-family:var(--serif);font-size:18px;color:#333;white-space:nowrap}
.blog-excerpt{position:absolute;left:26px;top:292px;width:275px;font-size:12.5px;line-height:22px;color:var(--muted)}
.more-btn{position:absolute;left:532px;top:2095px;width:137px;height:38px;background:var(--teal-soft);color:#1b7f6c;font-size:13px;display:flex;align-items:center;justify-content:center}

/* solutions */
.solutions{position:absolute;left:0;top:2186px;width:1200px;height:365px;background:var(--grey-bg)}
.sol-title{position:absolute;top:162px;font-family:var(--serif);font-size:20px}
.sol-text{position:absolute;top:200px;width:420px;font-size:12.5px;line-height:22px;color:var(--muted)}

/* footer */
.site-footer{position:absolute;left:0;top:2551px;width:1200px;height:297px;background:var(--footer);color:var(--footer-text);font-size:13px}
.foot-head{position:absolute;top:48px;color:#fff;font-family:var(--ui);font-size:17px}
.foot-head::after{content:"";position:absolute;left:0;top:30px;width:30px;height:1px;background:var(--teal)}
.foot-links{position:absolute;top:94px;list-style:none;line-height:27.5px}
.email-field{position:absolute;left:790px;top:100px;width:302px;border-bottom:1px solid #3b3a48;padding-bottom:10px;color:#6f6e7c}
.social{position:absolute;top:147px;width:24px;height:24px;border-radius:50%}
.foot-divider{position:absolute;left:89px;top:245px;width:1022px;height:1px;background:#34333f}
.foot-bottom{position:absolute;top:263px;font-size:12.5px}
.to-top{position:absolute;left:1139px;top:2778px;width:36px;height:36px;border-radius:50%;background:var(--orange);display:flex;align-items:center;justify-content:center}
</style>
</head>
<body>

<header class="site-header">
  <a class="nav-link active" style="left:89px">Home</a>
  <a class="nav-link" style="left:161px">About</a>
  <a class="nav-link" style="left:234px">Services &amp; Solutions</a>
  <a class="nav-link" style="left:389px">Blogs</a>
  <div class="brand"><span class="brand-dot"></span>Halvren</div>
  <a class="quote-link">Get a quote</a>
  <a class="contact-btn">Contact us</a>
</header>

<section class="hero">
  <div class="hero-photo" role="img" aria-label="Photo of a smiling family of four embracing against a light wall"></div>
  <h1 class="hero-title">Welcome to<br>Halvren Cunsolting</h1>
  <a class="hero-btn">Learn more</a>
  <div class="hero-dots"><span style="top:232px;background:#222"></span><span style="top:246px"></span><span style="top:260px"></span></div>
</section>

<section class="intro">
  <div class="rule" style="left:89px;top:670px"></div>
  <h2 class="intro-title">Short introduction<br>about our Startup</h2>
  <p class="intro-text" style="top:770px">Maecenas tempus tellus eget condimentum rhoncus sem quam semper libero sit amet adipiscing sem neque sed ipsum nam quam.</p>
  <p class="intro-text" style="top:826px">Aenean vulputate eleifend tellus aenean leo ligula porttitor eu consequat vitae eleifend ac enim aliquam lorem ante dapibus in viverra quis feugiat a tellus phasellus viverra nulla ut metus varius laoreet quisque rutrum aenean imperdi- et etiam ultricies nisi.</p>
  <a class="peach-btn">Learn More</a>
  <div class="media" style="left:822px;top:760px;width:177px;height:195px;background:var(--teal)"></div>
  <div class="media" role="img" aria-label="Photo of surgeons working under operating theatre lights" style="left:640px;top:680px;width:236px;height:258px;background:linear-gradient(135deg,#cfe3e3 0%,#4fb7b2 45%,#157f7c 100%);box-shadow:0 10px 24px rgba(0,0,0,.18)"></div>
  <div class="media" role="img" aria-label="Photo of a glucose meter, insulin pen and syringe on a table" style="left:934px;top:777px;width:177px;height:203px;background:linear-gradient(160deg,#e4e4e6 0%,#d2d3d6 60%,#c9a99a 100%);box-shadow:0 16px 30px rgba(0,0,0,.16)"></div>
</section>

<section class="services">
  <div class="rule" style="left:578px;top:84px;background:#fff"></div>
  <h2 class="section-title" style="top:94px;color:#fff;font-size:22px">Our Services</h2>

  <div class="service-icon" style="left:215px">
    <svg width="44" height="44" viewBox="0 0 44 44" fill="none" stroke="#1e6fa8" stroke-width="2"><circle cx="22" cy="10" r="5"/><circle cx="10" cy="32" r="5"/><circle cx="34" cy="32" r="5"/><path d="M22 15v6M18 22l-6 5M26 22l6 5" stroke="#f37321"/></svg>
  </div>
  <div class="service-label" style="left:110px">Public Consulting Services</div>
  <div class="dotline" style="left:390px;width:100px"></div>

  <div class="service-icon" style="left:553px">
    <svg width="44" height="44" viewBox="0 0 44 44"><rect x="9" y="8" width="26" height="30" rx="10" fill="#f37321"/><rect x="13" y="16" width="18" height="10" rx="4" fill="#2b2b3a"/><circle cx="18" cy="21" r="2" fill="#fff"/><circle cx="26" cy="21" r="2" fill="#fff"/></svg>
  </div>
  <div class="service-label" style="left:450px">Private Consulting Services</div>
  <div class="dotline" style="left:727px;width:100px"></div>

  <div class="service-icon" style="left:918px">
    <svg width="44" height="44" viewBox="0 0 44 44"><g transform="rotate(-40 22 22)"><rect x="8" y="15" width="28" height="14" rx="7" fill="#f3c1c1"/><path d="M22 15h7a7 7 0 010 14h-7z" fill="#e23a3a"/></g></svg>
  </div>
  <div class="service-label" style="left:813px">Access to Medicines</div>
</section>

<section class="blogs">
  <div class="rule" style="left:578px;top:1582px"></div>
  <h2 class="section-title" style="top:1596px">Latest Blogs</h2>

  <article class="blog-card" style="left:89px">
    <div class="blog-img" role="img" aria-label="Photo of medical staff in a bright hospital corridor" style="background:linear-gradient(120deg,#c9d3d8 0%,#8d9ca5 50%,#e8eef0 100%)"></div>
    <div class="blog-date">May<b>16th</b></div>
    <h3 class="blog-heading">Some blog heading here..</h3>
    <p class="blog-excerpt">Etiam ultricies nisi vel augue curabitur ullamcor- per ultricies nisi nam eget dui etiam rhoncus maecenas tempus tellus eget condim.</p>
  </article>

  <article class="blog-card lifted" style="left:439px">
    <div class="blog-img" role="img" aria-label="Photo of a modern operating room with green walls" style="background:linear-gradient(160deg,#dfeee4 0%,#6dbb74 45%,#2f6b44 100%)"></div>
    <div class="blog-date">May<b class="warm">16th</b></div>
    <h3 class="blog-heading">Some blog heading here..</h3>
    <p class="blog-excerpt">Etiam ultricies nisi vel augue curabitur ullamcor- per ultricies nisi nam eget dui etiam rhoncus maecenas tempus tellus eget condim.</p>
  </article>

  <article class="blog-card" style="left:788px">
    <div class="blog-img" role="img" aria-label="Photo of a gloved doctor holding an insulin pen" style="background:linear-gradient(135deg,#f1efec 0%,#dcd7d1 55%,#a89e95 100%)"></div>
    <div class="blog-date">May<b>16th</b></div>
    <h3 class="blog-heading">Some blog heading here..</h3>
    <p class="blog-excerpt">Etiam ultricies nisi vel augue curabitur ullamcor- per ultricies nisi nam eget dui etiam rhoncus maecenas tempus tellus eget condim.</p>
  </article>

  <a class="more-btn">View more Blogs</a>
</section>

<section class="solutions">
  <div class="rule" style="left:578px;top:74px"></div>
  <h2 class="section-title" style="top:86px">Solutions we provide</h2>

  <svg class="abs" style="left:89px;top:168px" width="48" height="48" viewBox="0 0 48 48"><circle cx="24" cy="24" r="24" fill="var(--teal)"/><path d="M24 12v24M12 24h24" stroke="#fff" stroke-width="7"/></svg>
  <h3 class="sol-title" style="left:154px">Access to Medical</h3>
  <p class="sol-text" style="left:154px">Lorem ipsum dolor sit amet consectetuer adipiscing elit aenean commodo ligula eget dolor aenean massa dum sociis natoque penatibus et magnis dis parturient montes nascetur ridiculus mus.</p>

  <svg class="abs" style="left:621px;top:168px" width="28" height="50" viewBox="0 0 28 50"><rect x="6" y="0" width="16" height="8" fill="#e6501f"/><rect x="3" y="8" width="22" height="4" fill="#c0400f"/><rect x="1" y="12" width="26" height="38" rx="3" fill="var(--orange)"/><rect x="5" y="22" width="18" height="14" fill="#fff"/></svg>
  <h3 class="sol-title" style="left:668px">Access to Health care</h3>
  <p class="sol-text" style="left:668px">Lorem ipsum dolor sit amet consectetuer adipiscing elit aenean commodo ligula eget dolor aenean massa dum sociis natoque penatibus et magnis dis parturient montes nascetur ridiculus mus.</p>
</section>

<footer class="site-footer">
  <h4 class="foot-head" style="left:89px">Information</h4>
  <ul class="foot-links" style="left:89px"><li>› Overview of Services</li><li>› Training</li><li>› About us</li><li>› Legal</li></ul>
  <ul class="foot-links" style="left:268px"><li>› Our Partners</li><li>› Protection</li><li>› Social Services</li></ul>

  <h4 class="foot-head" style="left:532px">Quick Links</h4>
  <ul class="foot-links" style="left:532px"><li>› Home</li><li>› About</li><li>› Quote</li><li>› Contact</li></ul>

  <h4 class="foot-head" style="left:790px">Follow &amp; Subscribe</h4>
  <div class="email-field">Enter your email address...</div>
  <svg class="abs" style="left:1072px;top:102px" width="16" height="16" viewBox="0 0 16 16"><path d="M1 8l14-6-5 13-2-5z" fill="var(--teal)"/></svg>
  <span class="social" style="left:789px;background:#3b5fa6"></span>
  <span class="social" style="left:821px;background:#2aa3e0"></span>
  <span class="social" style="left:853px;background:#d6372d"></span>

  <div class="foot-divider"></div>
  <div class="foot-bottom" style="left:89px">© 2017, All Rights Reserved.</div>
  <div class="foot-bottom" style="left:892px">Terms &amp; Conditions &nbsp;&nbsp; | &nbsp;&nbsp; Privacy policy</div>
</footer>

<a class="to-top" aria-label="Back to top"><svg width="12" height="12" viewBox="0 0 12 12"><path d="M6 10V2M2 6l4-4 4 4" stroke="#fff" stroke-width="1.6" fill="none"/></svg></a>

</body>
</html>
```